4"x9" Roofing Flyer Design - Tile Roofing!

We are looking to create a 4"x9" double sided flyer in full color that displays pictures of before and after of tile underlayment replacement. This would have words as well.

The theme should match the overall theme of our brochure that we already have designed so they are cohesive.

I have uploaded an example of a similar flyer that we like the overall layout of.

Please read the "Design Wording" PDF I uploaded for the words and overall design layout we are looking for on this brochure.

Please let me know if you'd like more photos or anything like that.

Target Market(s)

Retirees

Industry/Entity Type

Roofing

Font styles to use
Other font styles liked:
• Match existing fonts from our brochure

Requirements
Must have
• Must match style of existing brochure (uploaded), font must match closely as well

```html
<!DOCTYPE html>
<html lang="en">
<head>
<meta charset="utf-8">
<title>Tile Underlayment Flyer</title>
<link href="https://fonts.googleapis.com/css2?family=Raleway:wght@400;600;700&family=Arimo:wght@400;700&display=swap" rel="stylesheet">
<style>
:root{
  --stage:#cfcfd0;
  --green:#1f5a3c;
  --green-dark:#123d28;
  --green-bright:#138a5f;
  --label:#0f3424;
  --band:#a9a7aa;
  --ink:#1c1c1c;
  --paper:#ffffff;
}
*{box-sizing:border-box;margin:0;padding:0}
html,body{width:1200px;height:1200px;overflow:hidden;background:var(--stage)}
.flyer{position:absolute;top:22px;width:514px;height:1156px;background:var(--paper);font-family:"Raleway",sans-serif;color:var(--ink)}
.flyer--front{left:60px}
.flyer--back{left:631px}
.header{position:relative;height:184px;background:var(--green)}
.header__band{position:absolute;left:0;right:0;top:28px;height:107px;background:var(--band)}
.brand{position:absolute;left:18px;top:16px;width:187px;height:124px;display:flex;align-items:center;gap:10px;padding-left:10px}
.brand__mark{width:18px;height:18px;background:var(--green);flex:none}
.brand__name{font-family:"Raleway",sans-serif;font-weight:700;font-size:22px;line-height:1.1;color:var(--green-dark)}
.product{position:absolute;left:226px;top:36px;width:268px;text-align:center}
.product__name{font-family:"Arimo",sans-serif;font-weight:700;font-size:44px;line-height:48px;letter-spacing:1px;color:#2f2f2f;border-bottom:1.5px solid #3a3a3a;padding-bottom:6px}
.product__tag{font-family:"Arimo",sans-serif;font-size:17px;letter-spacing:1.5px;color:#3a3a3a;margin-top:5px}
.call{position:absolute;right:20px;top:168px;transform:translateY(-50%);font-family:"Arimo",sans-serif;font-weight:700;font-size:20px;color:#fff;display:flex;align-items:center;gap:6px;letter-spacing:-.3px}
.call svg{width:18px;height:18px}
.gallery{display:grid;grid-template-columns:256px 256px;grid-template-rows:242px 242px;column-gap:2px;row-gap:2px;height:486px}
.photo{position:relative}
.photo--before-a{background:linear-gradient(135deg,#8e877b,#b9b2a5 45%,#6a635a)}
.photo--before-b{background:linear-gradient(160deg,#6e5e4e,#9a8b79 50%,#7d7263)}
.photo--after-a{background:linear-gradient(170deg,#5b6f86 0%,#a3adb8 30%,#d2d6da 60%,#b9bec4)}
.photo--after-b{background:linear-gradient(150deg,#c7ac8d 0%,#b59a7d 50%,#9e8670)}
.photo__label{position:absolute;left:0;bottom:13px;width:81px;height:36px;background:var(--label);color:#fff;font-family:"Raleway",sans-serif;font-weight:700;font-size:17px;line-height:36px;padding-left:12px}
.copy{padding:29px 18px 0 18px}
.copy h2{font-size:18px;font-weight:600;line-height:22px;color:#151515}
.copy p{font-size:14.6px;line-height:21.5px}
.copy strong{font-weight:700}
.copy--problem h2{margin-bottom:18px}
.copy--problem p{margin-bottom:17px}
.copy--problem p.lead{margin-bottom:3px}
.copy--problem p.intro{margin-bottom:19px}
.copy--solution h2{margin-bottom:13px}
.copy--solution p{margin-bottom:12px}
.copy--solution p.lead{margin-bottom:8px}
.accent{position:absolute;left:0;right:0;bottom:0;height:17px}
.footer{position:absolute;left:0;right:0;bottom:0;height:33px;background:var(--green-bright);color:#fff;font-family:"Arimo",sans-serif;font-size:14px;display:flex;align-items:center;justify-content:space-between;padding:0 18px}
.footer__web{display:flex;align-items:center;gap:7px}
.footer__web svg{width:13px;height:13px}
</style>
</head>
<body>

<section class="flyer flyer--front">
  <header class="header">
    <div class="header__band"></div>
    <div class="brand"><span class="brand__mark"></span><span class="brand__name">Summit Shield Roofing</span></div>
    <div class="product"><div class="product__name">KORVANTE</div><div class="product__tag">Polyurethane Sealant</div></div>
    <div class="call">Call :
      <svg viewBox="0 0 24 24"><path fill="#fff" d="M3 8c0-2 4-4 9-4s9 2 9 4v2h-5V8.5c-1-.6-2.5-.9-4-.9s-3 .3-4 .9V10H3zm4 4h10l2 7H5zm5 1.5a2.5 2.5 0 100 5 2.5 2.5 0 000-5z"/></svg>
      (555) 014-2290</div>
  </header>
  <div class="gallery">
    <div class="photo photo--before-a" role="img" aria-label="Close-up of cracked, deteriorated underlayment beneath roof tiles"><span class="photo__label">Before</span></div>
    <div class="photo photo--before-b" role="img" aria-label="Crumbling old felt and debris under lifted tiles"><span class="photo__label">Before</span></div>
    <div class="photo photo--after-a" role="img" aria-label="New synthetic underlayment with battens installed across roof"><span class="photo__label">After</span></div>
    <div class="photo photo--after-b" role="img" aria-label="Finished roof with tan concrete tiles re-laid"><span class="photo__label">After</span></div>
  </div>
  <div class="copy copy--problem">
    <h2>The Hidden Clock Ticking Under Your Tiles</h2>
    <p class="lead">When a tile roof is installed, the tiles themselves are not waterproof—they are simply a shield. The actual waterproofing is done by the felt or synthetic underlayment installed beneath them.</p>
    <p class="intro">In homes of your vintage, this underlayment is now:</p>
    <p><strong>Brittle and Chalky:</strong>&nbsp; It cracks and turns into powder under the constant heat cycles, losing its waterproofing integrity.</p>
    <p><strong>Compromised:</strong> Even a single leak in a neighboring home means the moisture risk has increased exponentially across the entire block.</p>
    <p>Based on the age and materials used in this specific neighborhood, underlayment failure is not a matter of if, but when.</p>
    <p>Waiting for a visible ceiling stain often means the damage has already spread to the roof deck, rafters, and interior walls. A slow leak can silently cost thousands in remediation before you ever see a drop.</p>
  </div>
  <svg class="accent" viewBox="0 0 514 17" preserveAspectRatio="none">
    <polygon points="0,0 265,0 253,17 0,17" fill="var(--green-bright)"/>
    <polygon points="273,0 514,0 514,17 261,17" fill="var(--green-dark)"/>
  </svg>
</section>

<section class="flyer flyer--back">
  <header class="header">
    <div class="header__band"></div>
    <div class="brand"><span class="brand__mark"></span><span class="brand__name">Summit Shield Roofing</span></div>
    <div class="product"><div class="product__name">KORVANTE</div><div class="product__tag">Polyurethane Sealant</div></div>
    <div class="call">Call :
      <svg viewBox="0 0 24 24"><path fill="#fff" d="M3 8c0-2 4-4 9-4s9 2 9 4v2h-5V8.5c-1-.6-2.5-.9-4-.9s-3 .3-4 .9V10H3zm4 4h10l2 7H5zm5 1.5a2.5 2.5 0 100 5 2.5 2.5 0 000-5z"/></svg>
      (555) 014-2290</div>
  </header>
  <div class="gallery">
    <div class="photo photo--before-a" role="img" aria-label="Close-up of cracked, deteriorated underlayment beneath roof tiles"><span class="photo__label">Before</span></div>
    <div class="photo photo--before-b" role="img" aria-label="Crumbling old felt and debris under lifted tiles"><span class="photo__label">Before</span></div>
    <div class="photo photo--after-a" role="img" aria-label="New synthetic underlayment with battens installed across roof"><span class="photo__label">After</span></div>
    <div class="photo photo--after-b" role="img" aria-label="Finished roof with tan concrete tiles re-laid"><span class="photo__label">After</span></div>
  </div>
  <div class="copy copy--solution">
    <h2>Our Certified Solution: The Proactive, Full-Service Tile<br>Lift &amp; Re-Lay</h2>
    <p class="lead">We specialize in preserving your beautiful tile roof while replacing the single most important component: the underlayment.</p>
    <p>As a licensed, bonded, and insured local contractor, we don't just replace the felt; we ensure your entire roof is built to perform:</p>
    <p><strong>Careful Tile Removal:</strong> Each tile is removed by hand, inspected, and saved.</p>
    <p><strong>Deck Inspection:</strong> We check for and address any underlying damage or rot.</p>
    <p><strong>Premium Underlayment:</strong> We install a modern, high-grade self-adhered synthetic underlayment.</p>
    <p><strong>Tile Reinstallation:</strong> Your original, attractive tiles are re-laid with new flashings and seals, ready to perform for years.</p>
  </div>
  <footer class="footer">
    <span class="footer__web">
      <svg viewBox="0 0 24 24" fill="none" stroke="#fff" stroke-width="2"><circle cx="12" cy="12" r="10"/><path d="M2 12h20M12 2c3 3 3 17 0 20M12 2c-3 3-3 17 0 20"/></svg>
      www.ridgecrest-roofing.com</span>
    <span>AZ ROC 512077</span>
  </footer>
</section>

</body>
</html>
```